Larkhaven Meditation

Logo picture and I want it to say

yoga. meditation. sound healing

small sweet classes

Larkhaven-meditation.example

2417 West Orindale Ave Suite K
Santa Barbara ca 93108

```html
<!DOCTYPE html>
<html lang="en">
<head>
<meta charset="utf-8">
<title>Larkhaven Meditation – Business Card</title>
<link rel="stylesheet" href="https://fonts.googleapis.com/css2?family=Open+Sans:wght@400;600;700&family=Yeseva+One&display=swap">
<style>
  :root {
    --page-bg: #ecebef;
    --card-pink: #e07fc0;
    --card-magenta: #c95aae;
    --card-violet: #8b4fb0;
    --card-indigo: #6a54b3;
    --ink-light: #ffffff;
    --ornament-tint: rgba(255, 235, 250, 0.22);
    --ornament-ring: rgba(243, 214, 244, 0.35);
    --photo-light: #efe6df;
    --photo-mid: #d8c6b8;
    --photo-shadow: #9f8a82;
    --photo-rim: #d9c2ea;
  }

  * { box-sizing: border-box; margin: 0; padding: 0; }

  html, body {
    width: 1200px;
    height: 800px;
    overflow: hidden;
    background: var(--page-bg);
  }

  .canvas {
    position: relative;
    width: 1200px;
    height: 800px;
  }

  .business-card {
    position: absolute;
    left: 75px;
    top: 100px;
    width: 1050px;
    height: 600px;
    overflow: hidden;
    border-radius: 4px;
    background:
      radial-gradient(ellipse at 95% 0%, var(--card-magenta) 0%, transparent 55%),
      linear-gradient(160deg, var(--card-pink) 0%, var(--card-magenta) 35%, var(--card-violet) 70%, var(--card-indigo) 100%);
    box-shadow: 0 18px 40px rgba(60, 40, 80, 0.22);
    font-family: "Open Sans", sans-serif;
    color: var(--ink-light);
  }

  .ornament {
    position: absolute;
    background: radial-gradient(ellipse at center, var(--ornament-tint) 0%, rgba(255,235,250,0.08) 60%, transparent 75%);
  }
  .ornament--top { left: 270px; top: -50px; width: 360px; height: 200px; }
  .ornament--bottom { left: 230px; top: 470px; width: 360px; height: 200px; }
  .ornament--photo-ring {
    left: 540px; top: -130px; width: 640px; height: 640px;
    border-radius: 50%;
    background: radial-gradient(circle at center, transparent 44%, var(--ornament-ring) 46%, rgba(243,214,244,0.12) 62%, transparent 70%);
  }

  .photo-circle {
    position: absolute;
    left: 640px;
    top: -40px;
    width: 480px;
    height: 480px;
    border-radius: 50%;
    border: 5px solid var(--photo-rim);
    background:
      radial-gradient(ellipse at 70% 60%, var(--photo-shadow) 0%, transparent 45%),
      linear-gradient(135deg, var(--photo-light) 0%, var(--photo-mid) 60%, var(--photo-light) 100%);
  }

  .brand-mark {
    position: absolute;
    left: 80px;
    top: 60px;
    width: 160px;
    height: 160px;
    border: 3px solid var(--ink-light);
    border-radius: 50%;
    display: flex;
    align-items: center;
    justify-content: center;
    text-align: center;
  }
  .brand-mark__name {
    font-family: "Open Sans", sans-serif;
    font-weight: 600;
    font-size: 18px;
    line-height: 1.25;
    color: var(--ink-light);
  }

  .card-copy {
    position: absolute;
    left: 80px;
    top: 250px;
    width: 540px;
  }
  .services {
    font-family: "Open Sans", sans-serif;
    font-weight: 700;
    font-size: 21px;
    letter-spacing: 0.2px;
  }
  .headline {
    font-family: "Yeseva One", serif;
    font-weight: 400;
    font-size: 46px;
    letter-spacing: 1.5px;
    line-height: 1.15;
    margin-top: 6px;
    white-space: nowrap;
  }
  .address {
    font-style: normal;
    font-size: 21px;
    line-height: 1.35;
    margin-top: 14px;
  }
  .website {
    font-size: 17px;
    margin-top: 20px;
  }
</style>
</head>
<body>
  <main class="canvas">
    <article class="business-card">
      <div class="ornament ornament--top" role="img" aria-label="Decorative mandala pattern in pale lilac line work"></div>
      <div class="ornament ornament--bottom" role="img" aria-label="Decorative mandala pattern in pale lilac line work"></div>
      <div class="ornament ornament--photo-ring" role="img" aria-label="Mandala petals framing the class photo"></div>
      <div class="photo-circle" role="img" aria-label="Photo of a row of women meditating cross-legged in a bright studio"></div>

      <div class="brand-mark">
        <span class="brand-mark__name">Larkhaven<br>Meditation</span>
      </div>

      <div class="card-copy">
        <p class="services">Yoga . Meditation . Sound Healing</p>
        <h1 class="headline">Small Sweet Classes</h1>
        <address class="address">
          2417 West Orindale Ave Suite K<br>
          Santa Barbara ca 93108
        </address>
        <p class="website">www.larkhaven-meditation.example</p>
      </div>
    </article>
  </main>
</body>
</html>
```